Personal Injury Law Firm needs folder design

Need a folder design for our personal injury law firm, Torrin & Mapley, LLC. to give to all of our clients with their documents at the end of their case. I've attached our branding guide. We are branded as the 5 star law firm that fights for our clients like family. It should incorporate our colors or Green and White. We'd like to convey a message of moving on to the next chapter after finishing their case.

```html
<!DOCTYPE html>
<html lang="en">
<head>
<meta charset="utf-8">
<title>Torrin &amp; Mapley, LLC. — Client Folder</title>
<link rel="stylesheet" href="https://fonts.googleapis.com/css2?family=Cinzel:wght@500&family=Open+Sans:wght@500&display=swap">
<style>
  :root {
    --brand-green: #3aa37a;
    --paper: #ffffff;
    --ink: #2b2f33;
    --stage: #ececec;
    --badge: #e4e9e6;
    --photo-navy-dark: #1d2538;
    --photo-navy-light: #4a5468;
    --photo-grey-dark: #2a2e36;
    --photo-grey-light: #8d939c;
  }
  html, body {
    margin: 0;
    width: 1200px;
    height: 962px;
    overflow: hidden;
    background: var(--stage);
  }
  .folder-spread {
    position: absolute;
    left: 181px;
    top: 107px;
    width: 838px;
    height: 747px;
  }
  .panel-paper { fill: var(--paper); }
  .accent { fill: var(--brand-green); }
  .firm-name {
    font-family: "Cinzel", serif;
    font-weight: 500;
    fill: var(--brand-green);
  }
  .contact-text {
    font-family: "Open Sans", sans-serif;
    font-weight: 500;
    font-size: 17px;
    fill: var(--ink);
  }
  .contact-icon { fill: none; stroke: var(--brand-green); stroke-width: 1.6; }
  .contact-icon-solid { fill: var(--brand-green); }
  .rating-badge { fill: var(--badge); }
</style>
</head>
<body>
<svg class="folder-spread" viewBox="385 203 1506 1342" xmlns="http://www.w3.org/2000/svg">
  <defs>
    <linearGradient id="team-duo-tones" x1="0" y1="0" x2="0" y2="1">
      <stop offset="0" stop-color="var(--photo-navy-light)"/>
      <stop offset="1" stop-color="var(--photo-navy-dark)"/>
    </linearGradient>
    <linearGradient id="team-walk-tones" x1="0" y1="0" x2="0" y2="1">
      <stop offset="0" stop-color="var(--photo-grey-dark)"/>
      <stop offset="0.5" stop-color="var(--photo-navy-light)"/>
      <stop offset="1" stop-color="var(--photo-grey-light)"/>
    </linearGradient>
  </defs>

  <!-- Back cover -->
  <g class="back-cover">
    <rect class="panel-paper" x="435" y="203" width="728" height="1010"/>
    <polygon class="accent" points="435,203 621,203 645,228 475,400 435,361"/>
    <polygon class="accent" points="722,203 1163,203 1163,490 1085,565"/>
    <polygon points="703,411 971,679 703,947 435,679" fill="url(#team-duo-tones)"
             role="img" aria-label="Photo of two attorneys in dark suits smiling"/>

    <g class="brand-lockup">
      <rect class="accent" x="539" y="963" width="60" height="50"/>
      <text class="firm-name" x="609" y="994" font-size="16">TORRIN &amp; MAPLEY, LLC.</text>
    </g>

    <rect class="rating-badge" x="890" y="950" width="185" height="72" rx="6"
          role="img" aria-label="Five-star firm badge"/>

    <g class="contact-list">
      <path class="contact-icon" d="M535 1054 q2 -3 4 0 l1 3 q-1 2 1 4 q2 2 4 1 l3 1 q3 2 0 4 q-5 3 -10 -3 q-6 -5 -3 -10z"/>
      <text class="contact-text" x="557" y="1065">(555) 014-2290</text>

      <rect class="contact-icon" x="534" y="1082" width="13" height="9"/>
      <path class="contact-icon" d="M534 1082 l6.5 5 l6.5 -5"/>
      <text class="contact-text" x="557" y="1094">dana@torrinandmapley.com</text>

      <circle class="contact-icon" cx="540" cy="1117" r="6.5"/>
      <path class="contact-icon" d="M533.5 1117 h13 M540 1110.5 q-4 6.5 0 13 q4 -6.5 0 -13"/>
      <text class="contact-text" x="557" y="1123">www.torrinandmapley.com</text>

      <path class="contact-icon-solid" d="M902 1051 a6 6 0 0 1 6 6 q0 4 -6 11 q-6 -7 -6 -11 a6 6 0 0 1 6 -6z"/>
      <circle cx="902" cy="1057" r="2.2" fill="var(--paper)"/>
      <text class="contact-text" x="918" y="1065">4120 Harbor Crest Lane</text>
      <text class="contact-text" x="918" y="1094">Cedar Bay, FL 30419</text>
    </g>
  </g>

  <!-- Front cover -->
  <g class="front-cover">
    <rect class="panel-paper" x="1163" y="203" width="728" height="1010"/>
    <polygon class="accent" points="1163,203 1448,203 1163,488"/>
    <polygon class="accent" points="1581,203 1891,203 1891,510"/>
    <polygon points="1527,205 1890,565 1527,930 1163,565" fill="url(#team-walk-tones)"
             role="img" aria-label="Photo of a legal team in suits walking through an office"/>
    <polygon points="1163,615 1336,787 1163,960" fill="url(#team-walk-tones)"
             role="img" aria-label="Office floor detail continuing the team photo"/>
    <polygon class="accent" points="1891,590 1782,700 1891,805"/>
    <polygon class="accent" points="1770,717 1891,838 1891,892 1770,1013 1618,865"/>
    <polygon class="accent" points="1891,925 1785,1025 1891,1130"/>

    <g class="brand-lockup">
      <rect class="accent" x="1218" y="990" width="100" height="82"/>
      <text class="firm-name" x="1332" y="1040" font-size="22">TORRIN &amp; MAPLEY, LLC.</text>
    </g>
  </g>

  <!-- Inside pocket -->
  <polygon class="accent pocket" points="385,1230 435,1213 1157,1213 1108,1545 435,1545 385,1530"/>
</svg>
</body>
</html>
```